A start-up named "Corvath Therapeutics" - needs a new PowerPoint design

We need a new PowerPoint Design for an early-stage start-up named "Corvath Therapeutics" seeking to disrupt the current approach towards drug discovery within aging disorders.

We would like to build on Corvath's legacy, the founder of the modern science of genetics, by employing a multidisciplinary approach, experimenting, and providing elderly patients the attention they deserve.

We have selected the suffix "therapeutics" intentionally as it stands for (a medicine) the treatment of disease; the science of healing. Alzheimer’s treatment is a huge, urgent, unmet need:
- Shift from a disease-management system to a preventive medicine system
- Focus on increasing the health span, not only the life span

Target Market(s)

Pharma/ Biotech Executives Medical Institutions Healthcare professionals (MDs, nurses, payors, pharmacists, etc.) Patients

Industry/Entity Type

Healthcare

Other font styles liked:
• Celias

Colors
0054AA
0677BA
7BADD7
CADEEF
E8F1F8
E54698
E96AAD
F1A4CE
F9D9EA
FCEFF6
A7469A
B969AE
D3A5CF
EDDBEB
F8F0F9
6B429C
8869AF
B7A5CE
E3DAEB
F3F0F8

Requirements
Must have
• - differentiate from other companies named after Corvath - differentiate from other Pharma/ Biotech companies
Nice to have
• simplicity/ minimalist logo vivid colors gradient 3D Life-Sciences inspired Simple geometry Balance
Should not have
• mascot/ emblem watermark logo animated ink style nature-inspired inventive typography artistic chaos

```html
<!DOCTYPE html>
<html lang="en">
<head>
<meta charset="utf-8">
<title>Corvath Therapeutics – Presentation Design</title>
<link href="https://fonts.googleapis.com/css2?family=Lexend:wght@300;400;500;600&display=swap" rel="stylesheet">
<style>
:root{
  --blue:#0054AA;
  --blue-mid:#0677BA;
  --blue-light:#7BADD7;
  --pink:#E54698;
  --pink-soft:#E96AAD;
  --purple:#A7469A;
  --purple-mid:#B969AE;
  --lilac:#D3A5CF;
  --violet:#6B429C;
  --ink:#1a1a1a;
  --grey:#555;
  --grey-light:#efeff2;
  --white:#fff;
  --stage:#e3e5eb;
}
*{box-sizing:border-box;margin:0;padding:0}
html,body{width:675px;height:1200px;overflow:hidden}
body{background:var(--stage);font-family:'Lexend',sans-serif;position:relative;color:var(--ink)}

/* header brand block */
.brand-lockup{position:absolute;left:503px;top:46px;display:flex;align-items:center;gap:6px;color:var(--blue)}
.brand-lockup .mark{width:30px;height:30px;background:var(--blue)}
.brand-lockup .name{font-weight:500;font-size:20px;line-height:1}
.brand-lockup .name small{display:block;font-size:10.5px;letter-spacing:1px;margin-top:2px}
.swatches{position:absolute;left:503px;top:103px;display:flex;gap:9px}
.swatches span{width:13px;height:13px;border-radius:50%}

/* hero slide */
.hero{position:absolute;left:40px;top:80px;width:420px;height:236px;background:var(--white);overflow:hidden;box-shadow:0 8px 24px rgba(0,0,0,.12)}

/* slides */
.slide{position:absolute;width:210px;height:118px;background:var(--white);overflow:hidden}
.slide-title{position:absolute;left:11px;top:8px;font-size:8.4px;font-weight:400;color:var(--blue);white-space:nowrap}
.slide-title em{font-style:normal;color:var(--purple-mid)}
.mini-brand{position:absolute;right:11px;top:9px;display:flex;align-items:center;gap:1.5px;font-size:4.2px;font-weight:500;color:var(--blue)}
.mini-brand i{display:block;width:5px;height:5px;background:var(--blue)}
.footer{position:absolute;left:0;right:0;bottom:0;height:5.5px;background:linear-gradient(90deg,#3d4fa6,var(--violet) 50%,var(--purple-mid));font-size:1.8px;color:#fff;padding-left:2px;line-height:5.5px}
.footer .page{position:absolute;right:0;top:0;bottom:0;width:17px;background:var(--blue);text-align:center}
.txt{font-size:2.5px;line-height:1.3;color:var(--grey)}
.abs{position:absolute}
.h-blue{color:var(--blue);font-weight:500}
.h-purple{color:var(--purple-mid);font-weight:500}
.h-lilac{color:var(--lilac);font-weight:500}
.photo{position:absolute}
ul.bul{list-style:none}
ul.bul li{position:relative;padding-left:3px;margin-bottom:1.4px}
ul.bul li::before{content:"";position:absolute;left:0;top:1px;width:1.2px;height:1.2px;border-radius:50%;background:var(--blue)}

/* title slide text */
.cover-brand{position:absolute;left:13px;top:20px;display:flex;align-items:center;gap:2px;font-size:6px;font-weight:500;line-height:1}
.cover-brand i{display:block;width:9px;height:9px}
.cover-title{position:absolute;left:13px;top:48px;font-size:11px;font-weight:600;line-height:1.05}
.cover-date{position:absolute;left:13px;top:74px;font-size:2.2px}
.cover-copy{position:absolute;left:13px;top:97px;font-size:1.8px}

/* agenda */
.agenda-item{position:absolute;display:flex;gap:6px;align-items:flex-start}
.agenda-item b{font-size:8px;font-weight:300;color:#bbb;line-height:1}
.agenda-item .t{font-size:4.2px}

/* team */
.member{position:absolute;top:34px;width:56px;text-align:center}
.member .avatar{width:27px;height:27px;border-radius:50%;margin:0 auto 3px;background:radial-gradient(circle at 50% 40%,#c9b8aa,#6d7078)}
.member .n{font-size:4px}
.member .r{font-size:2.5px;color:var(--grey);margin:1px 0 2px}

/* icon features */
.feature{position:absolute;top:53px;width:40px;text-align:center}
.feature .dot{width:15px;height:15px;border-radius:50%;margin:0 auto 2px}
.feature .hd{font-size:4.3px;font-weight:500;margin-bottom:2px}

/* timeline */
.tl-dot{position:absolute;top:60px;width:9px;height:9px;border-radius:50%;color:#fff;font-size:5px;text-align:center;line-height:9px}
.tl-text{position:absolute;width:34px;text-align:center;font-size:3.4px;font-weight:500;line-height:1.05}

/* table */
table.data{position:absolute;left:16px;top:32px;width:196px;border-collapse:collapse;font-size:2.5px}
table.data td{height:6.5px;padding:0 2px;border-bottom:.3px solid #ddd;text-align:center;color:var(--pink)}
table.data td:first-child{text-align:left;color:var(--ink)}

/* contact */
.contact-line{display:flex;align-items:center;gap:3px;font-size:2.6px;color:#fff;margin-bottom:2.5px}
</style>
</head>
<body>

<!-- header brand + palette -->
<div class="brand-lockup">
  <span class="mark"></span>
  <div class="name">Corvath<small>Therapeutics</small></div>
</div>
<div class="swatches">
  <span style="background:var(--blue)"></span>
  <span style="background:var(--purple-mid)"></span>
  <span style="background:var(--lilac)"></span>
  <span style="background:var(--pink)"></span>
  <span style="background:var(--blue-light)"></span>
  <span style="background:var(--violet)"></span>
</div>

<!-- hero cover, flat -->
<section class="hero">
  <svg width="420" height="236" viewBox="0 0 210 118" preserveAspectRatio="none">
    <defs>
      <linearGradient id="lab" x1="0" y1="0" x2="1" y2="1"><stop offset="0" stop-color="#cfd6de"/><stop offset=".6" stop-color="#9aa6b6"/><stop offset="1" stop-color="#6f7e93"/></linearGradient>
    </defs>
    <rect role="img" aria-label="Photo of a scientist in a lab coat and mask in a pharmacy" x="60" y="0" width="150" height="118" fill="url(#lab)"/>
    <polygon points="95,118 122,118 182,36 168,26" fill="#B969AE" opacity=".75"/>
    <polygon points="70,0 110,0 150,59 138,59" fill="#0054AA"/>
    <polygon points="0,0 70,0 138,59 70,118 0,118" fill="#fff"/>
  </svg>
  <div class="cover-brand" style="left:26px;top:40px;font-size:12px;color:var(--blue);gap:4px"><i style="width:18px;height:18px;background:var(--blue)"></i>Corvath Therapeutics</div>
  <div class="cover-title" style="left:26px;top:96px;font-size:22px"><span style="color:var(--blue)">Corvath</span><br><span style="color:var(--purple-mid)">Therapeutics</span></div>
  <div class="cover-date" style="left:26px;top:148px;font-size:4.4px;color:var(--violet)">Monday, January 17, 2022</div>
  <div class="cover-copy" style="left:26px;top:194px;font-size:3.6px;color:#bbb">© 2021 Corvath Therapeutics, All Rights Reserved.</div>
</section>

<!-- row 1: covers -->
<section class="slide" style="left:15px;top:440px">
  <svg class="abs" width="210" height="118" viewBox="0 0 210 118">
    <rect role="img" aria-label="Photo of a scientist reading a tablet in a pharmacy" x="60" y="0" width="150" height="118" fill="url(#lab)"/>
    <polygon points="95,118 122,118 182,36 168,26" fill="#B969AE" opacity=".75"/>
    <polygon points="70,0 110,0 150,59 138,59" fill="#0054AA"/>
    <polygon points="0,0 70,0 138,59 70,118 0,118" fill="#fff"/>
  </svg>
  <div class="cover-brand" style="color:var(--blue)"><i style="background:var(--blue)"></i>Corvath Therapeutics</div>
  <div class="cover-title"><span style="color:var(--blue)">Corvath</span><br><span style="color:var(--purple-mid)">Therapeutics</span></div>
  <div class="cover-date" style="color:var(--violet)">Monday, January 17, 2022</div>
  <div class="cover-copy" style="color:#bbb">© 2021 Corvath Therapeutics, All Rights Reserved.</div>
</section>

<section class="slide" style="left:232px;top:440px">
  <svg class="abs" width="210" height="118" viewBox="0 0 210 118">
    <defs><linearGradient id="lab2" x1="0" y1="0" x2="1" y2="1"><stop offset="0" stop-color="#8fa3bd"/><stop offset="1" stop-color="#3c4d66"/></linearGradient></defs>
    <rect role="img" aria-label="Photo of a researcher working with samples in a laboratory" x="60" y="0" width="150" height="118" fill="url(#lab2)"/>
    <polygon points="95,118 122,118 182,36 168,26" fill="#B969AE" opacity=".75"/>
    <polygon points="70,0 110,0 150,59 138,59" fill="#0054AA"/>
    <polygon points="0,0 70,0 138,59 70,118 0,118" fill="#000"/>
  </svg>
  <div class="cover-brand" style="color:#fff"><i style="background:#fff"></i>Corvath Therapeutics</div>
  <div class="cover-title"><span style="color:#fff">Corvath</span><br><span style="color:var(--purple-mid)">Therapeutics</span></div>
  <div class="cover-date" style="color:#fff">Monday, January 17, 2022</div>
  <div class="cover-copy" style="color:#fff">© 2021 Corvath Therapeutics, All Rights Reserved.</div>
</section>

<section class="slide" style="left:450px;top:440px">
  <svg class="abs" width="210" height="118" viewBox="0 0 210 118">
    <defs><linearGradient id="lab3" x1="0" y1="0" x2="1" y2="1"><stop offset="0" stop-color="#b7bcc6"/><stop offset="1" stop-color="#5e6675"/></linearGradient></defs>
    <rect role="img" aria-label="Photo of hands holding a tablet in a clinic" x="60" y="0" width="150" height="118" fill="url(#lab3)"/>
    <polygon points="95,118 122,118 182,36 168,26" fill="#B969AE" opacity=".75"/>
    <polygon points="70,0 110,0 150,59 138,59" fill="#0677BA"/>
    <polygon points="0,0 70,0 138,59 70,118 0,118" fill="#0054AA"/>
  </svg>
  <div class="cover-brand" style="color:#fff"><i style="background:#fff"></i>Corvath Therapeutics</div>
  <div class="cover-title" style="color:#fff">Corvath<br>Therapeutics</div>
  <div class="cover-date" style="color:#fff">Monday, January 17, 2022</div>
  <div class="cover-copy" style="color:#fff">© 2021 Corvath Therapeutics, All Rights Reserved.</div>
</section>

<!-- row 2 -->
<section class="slide" style="left:15px;top:566px">
  <h2 class="slide-title">Agenda <em>Slide</em></h2>
  <div class="mini-brand"><i></i>Corvath</div>
  <div class="agenda-item" style="left:28px;top:36px"><b>1</b><div class="t h-blue">Title Goes Here<div class="txt" style="font-size:2.3px;font-weight:300">Lorem ipsum dolor sit amet, consectetur<br>adipiscing elit. Vivamus eu dui ex.</div></div></div>
  <div class="agenda-item" style="left:111px;top:36px"><b>2</b><div class="t h-purple">Title Goes Here<div class="txt" style="font-size:2.3px;font-weight:300">Lorem ipsum dolor sit amet, consectetur<br>adipiscing elit. Vivamus eu dui ex.</div></div></div>
  <div class="agenda-item" style="left:28px;top:57px"><b>3</b><div class="t h-purple">Title Goes Here<div class="txt" style="font-size:2.3px;font-weight:300">Lorem ipsum dolor sit amet, consectetur<br>adipiscing elit. Vivamus eu dui ex.</div></div></div>
  <div class="agenda-item" style="left:111px;top:57px"><b>4</b><div class="t h-blue">Title Goes Here<div class="txt" style="font-size:2.3px;font-weight:300">Lorem ipsum dolor sit amet, consectetur<br>adipiscing elit. Vivamus eu dui ex.</div></div></div>
  <div class="agenda-item" style="left:28px;top:78px"><b>5</b><div class="t h-blue">Title Goes Here<div class="txt" style="font-size:2.3px;font-weight:300">Lorem ipsum dolor sit amet, consectetur<br>adipiscing elit. Vivamus eu dui ex.</div></div></div>
  <div class="agenda-item" style="left:111px;top:78px"><b>6</b><div class="t h-purple">Title Goes Here<div class="txt" style="font-size:2.3px;font-weight:300">Lorem ipsum dolor sit amet, consectetur<br>adipiscing elit. Vivamus eu dui ex.</div></div></div>
  <div class="footer">© 2021 Corvath Therapeutics, All Rights Reserved.<span class="page">4</span></div>
</section>

<section class="slide" style="left:232px;top:566px">
  <div class="photo" role="img" aria-label="Photo of a researcher at a lab bench" style="left:13px;top:0;width:111px;height:63px;background:linear-gradient(135deg,#a9b8cc,#4f627c)"></div>
  <div class="photo" role="img" aria-label="Photo of a tablet in use" style="left:13px;top:66px;width:48px;height:32px;background:linear-gradient(135deg,#c2c7cf,#6b7384)"></div>
  <div class="photo" role="img" aria-label="Photo of a pharmacist between shelves" style="left:63px;top:66px;width:48px;height:32px;background:linear-gradient(135deg,#d7dde4,#8b97a6)"></div>
  <div class="mini-brand"><i></i>Corvath</div>
  <h2 class="slide-title" style="left:120px;top:30px"><span style="color:var(--blue)">About</span> <em>Us</em></h2>
  <div class="txt abs" style="left:120px;top:42px;width:78px">Lorem ipsum dolor sit amet, consectetur adipiscing elit. Vivamus eu dui ex. Curabitur dapibus dignissim dui, in molestie metus feugiat sed. Praesent aliquet lorem ex, eu dapibus.
    <ul class="bul" style="margin-top:2px">
      <li>Lorem ipsum dolor sit amet, consectetur adipiscing elit. Vivamus eu dui ex.</li>
      <li>Curabitur dapibus dignissim dui, in molestie metus feugiat sed.</li>
      <li>Praesent aliquet lorem ex, eu dapibus odio varius at. Duis eget tellus porta.</li>
      <li>Nulla facilisi. In et sollicitudin lacus. Donec risus orci, gravida sit amet.</li>
    </ul>
  </div>
  <div class="footer">© 2021 Corvath Therapeutics, All Rights Reserved.<span class="page">5</span></div>
</section>

<section class="slide" style="left:450px;top:566px">
  <h2 class="slide-title">Meet <em style="color:var(--blue)">Our</em> <em>Team</em></h2>
  <div class="mini-brand"><i></i>Corvath</div>
  <div class="member" style="left:15px"><div class="avatar" role="img" aria-label="Portrait of a team member"></div><div class="n h-blue">Name Goes Here</div><div class="r">Job Title Goes Here</div><div class="txt">Lorem ipsum dolor sit amet, consectetur adipiscing elit. Vivamus eu dui ex. Curabitur dapibus dignissim dui, in molestie metus feugiat sed.</div></div>
  <div class="member" style="left:77px"><div class="avatar" role="img" aria-label="Portrait of a team member"></div><div class="n h-purple">Name Goes Here</div><div class="r">Job Title Goes Here</div><div class="txt">Lorem ipsum dolor sit amet, consectetur adipiscing elit. Vivamus eu dui ex. Curabitur dapibus dignissim dui, in molestie metus feugiat sed.</div></div>
  <div class="member" style="left:139px"><div class="avatar" role="img" aria-label="Portrait of a team member"></div><div class="n h-lilac">Name Goes Here</div><div class="r">Job Title Goes Here</div><div class="txt">Lorem ipsum dolor sit amet, consectetur adipiscing elit. Vivamus eu dui ex. Curabitur dapibus dignissim dui, in molestie metus feugiat sed.</div></div>
  <div class="footer">© 2021 Corvath Therapeutics, All Rights Reserved.<span class="page">6</span></div>
</section>

<!-- row 3 -->
<section class="slide" style="left:15px;top:691px">
  <h2 class="slide-title">Slide Title <em>Goes Here</em></h2>
  <div class="mini-brand"><i></i>Corvath</div>
  <ul class="bul txt abs" style="left:11px;top:25px;width:92px">
    <li>Lorem ipsum dolor sit amet, consectetur adipiscing elit. Vivamus eu dui ex. Curabitur dapibus dignissim dui, in molestie metus feugiat sed.</li>
    <li>Praesent aliquet lorem ex, eu dapibus odio varius at. Duis eget tellus porta, consequat lacus vitae, venenatis dolor.</li>
    <li>Lorem ipsum dolor sit amet, consectetur adipiscing elit. Vivamus eu dui ex. Curabitur dapibus dignissim dui, in molestie metus feugiat sed.</li>
  </ul>
  <div class="photo" role="img" aria-label="Photo of a scientist at a computer screen" style="left:117px;top:25px;width:76px;height:48px;background:linear-gradient(135deg,#5d7fa6,#23344f)"></div>
  <div class="abs txt" style="left:0;top:67px;width:193px;height:32px;background:var(--blue);color:#fff;padding:5px 8px 0 19px;font-size:2.6px">Lorem ipsum dolor sit amet, consectetur adipiscing elit. Vivamus eu dui ex. Curabitur dapibus dignissim dui, in molestie metus feugiat sed. Praesent aliquet lorem ex, eu dapibus odio varius at. Duis eget tellus porta, consequat lacus vitae, venenatis dolor. Nulla facilisi. In et sollicitudin lacus. Donec risus orci, gravida sit amet risus vehicula, aliquet pretium sapien. Nullam sit amet magna non ex bibendum mollis.</div>
  <div class="abs" style="left:193px;top:67px;width:17px;height:32px;background:var(--purple-mid)"></div>
  <div class="footer">© 2021 Corvath Therapeutics, All Rights Reserved.<span class="page">7</span></div>
</section>

<section class="slide" style="left:232px;top:691px">
  <h2 class="slide-title">Slide Title <em>Goes Here</em></h2>
  <div class="mini-brand"><i></i>Corvath</div>
  <div class="txt abs" style="left:22px;top:32px;width:166px;text-align:center;font-size:2.9px">Lorem ipsum dolor sit amet, consectetur adipiscing elit. Vivamus eu dui ex. Curabitur dapibus dignissim dui, in molestie metus feugiat sed. Praesent aliquet lorem ex, eu dapibus odio varius at. Duis eget tellus porta, consequat lacus vitae, venenatis dolor.</div>
  <div class="feature" style="left:16px"><div class="dot" style="background:var(--blue)"></div><div class="hd" style="color:var(--blue)">Heading</div><div class="txt" style="font-size:2.2px">Lorem ipsum dolor sit amet, consectetur adipiscing elit. Vivamus eu dui ex. Curabitur dapibus dignissim dui.</div></div>
  <div class="feature" style="left:63px"><div class="dot" style="background:var(--purple-mid)"></div><div class="hd" style="color:var(--purple-mid)">Heading</div><div class="txt" style="font-size:2.2px">Lorem ipsum dolor sit amet, consectetur adipiscing elit. Vivamus eu dui ex. Curabitur dapibus dignissim dui.</div></div>
  <div class="feature" style="left:110px"><div class="dot" style="background:var(--lilac)"></div><div class="hd" style="color:var(--lilac)">Heading</div><div class="txt" style="font-size:2.2px">Lorem ipsum dolor sit amet, consectetur adipiscing elit. Vivamus eu dui ex. Curabitur dapibus dignissim dui.</div></div>
  <div class="feature" style="left:157px"><div class="dot" style="background:var(--pink)"></div><div class="hd" style="color:var(--pink)">Heading</div><div class="txt" style="font-size:2.2px">Lorem ipsum dolor sit amet, consectetur adipiscing elit. Vivamus eu dui ex. Curabitur dapibus dignissim dui.</div></div>
  <div class="footer">© 2021 Corvath Therapeutics, All Rights Reserved.<span class="page">8</span></div>
</section>

<section class="slide" style="left:450px;top:691px">
  <h2 class="slide-title">Slide Title <em>Goes Here</em></h2>
  <div class="mini-brand"><i></i>Corvath</div>
  <div class="txt abs" style="left:11px;top:25px;width:188px;font-size:2.3px">Lorem ipsum dolor sit amet, consectetur adipiscing elit. Vivamus eu dui ex. Curabitur dapibus dignissim dui, in molestie metus feugiat sed. Praesent aliquet lorem ex, eu dapibus odio varius at. Duis eget tellus porta, consequat lacus vitae, venenatis dolor. Nulla facilisi. In et sollicitudin lacus.<br><br>Donec risus orci, gravida sit amet risus vehicula, aliquet pretium sapien. Nullam sit amet magna non ex bibendum mollis. Nunc vel neque eu augue dignissim congue ut vitae magna. Integer venenatis, tellus sit amet interdum pretium, erat neque rhoncus turpis.</div>
  <div class="photo" role="img" aria-label="Photo of laboratory equipment and sample racks" style="left:0;top:55px;width:108px;height:42px;background:linear-gradient(135deg,#b5c1d0,#3f5878)"></div>
  <div class="abs" style="left:108px;top:55px;width:98px;height:42px;background:linear-gradient(90deg,var(--blue),#3a4fa8 60%,var(--violet));color:#fff;font-size:4.4px;line-height:1.15;padding:6px 7px">Lorem ipsum dolor sit amet, consectetur adipiscing elit. Vivamus eu dui ex. Curabitur dapibus dignissim dui, in molestie metus.</div>
  <div class="footer">© 2021 Corvath Therapeutics, All Rights Reserved.<span class="page">9</span></div>
</section>

<!-- row 4 -->
<section class="slide" style="left:15px;top:816px">
  <h2 class="slide-title">Slide Title <em>Goes Here</em></h2>
  <div class="mini-brand"><i></i>Corvath</div>
  <div class="abs" style="left:11px;top:33px;width:58px"><div class="h-blue" style="font-size:3.8px;margin-bottom:3px">Title Goes Here!</div><ul class="bul txt"><li>Lorem ipsum dolor sit amet, consectetur adipiscing elit. Vivamus eu dui ex. Curabitur dapibus dignissim dui, in molestie metus feugiat sed.</li><li>Praesent aliquet lorem ex, eu dapibus odio varius at. Duis eget tellus porta, consequat lacus vitae, venenatis dolor.</li><li>Nulla facilisi. In et sollicitudin lacus. Donec risus orci, gravida sit amet risus vehicular.</li><li>Nullam sit amet magna non ex bibendum mollis.</li></ul></div>
  <div class="abs" style="left:72px;top:33px;width:.3px;height:60px;background:#ccc"></div>
  <div class="abs" style="left:76px;top:33px;width:58px"><div class="h-purple" style="font-size:3.8px;margin-bottom:3px">Title Goes Here!</div><ul class="bul txt"><li>Lorem ipsum dolor sit amet, consectetur adipiscing elit. Vivamus eu dui ex. Curabitur dapibus dignissim dui, in molestie metus feugiat sed.</li><li>Praesent aliquet lorem ex, eu dapibus odio varius at. Duis eget tellus porta, consequat lacus vitae, venenatis dolor.</li><li>Nulla facilisi. In et sollicitudin lacus. Donec risus orci, gravida sit amet risus vehicular.</li><li>Nullam sit amet magna non ex bibendum mollis.</li></ul></div>
  <div class="abs" style="left:137px;top:33px;width:.3px;height:60px;background:#ccc"></div>
  <div class="abs" style="left:141px;top:33px;width:58px"><div class="h-lilac" style="font-size:3.8px;margin-bottom:3px">Title Goes Here!</div><ul class="bul txt"><li>Lorem ipsum dolor sit amet, consectetur adipiscing elit. Vivamus eu dui ex. Curabitur dapibus dignissim dui, in molestie metus feugiat sed.</li><li>Praesent aliquet lorem ex, eu dapibus odio varius at. Duis eget tellus porta, consequat lacus vitae, venenatis dolor.</li><li>Nulla facilisi. In et sollicitudin lacus. Donec risus orci, gravida sit amet risus vehicular.</li><li>Nullam sit amet magna non ex bibendum mollis.</li></ul></div>
  <div class="footer">© 2021 Corvath Therapeutics, All Rights Reserved.<span class="page">10</span></div>
</section>

<section class="slide" style="left:232px;top:816px">
  <h2 class="slide-title">Slide Title <em>Goes Here</em></h2>
  <div class="mini-brand"><i></i>Corvath</div>
  <div class="abs txt" style="left:42px;top:31px;width:24px;font-size:2px">✓ Lorem ipsum dolor sit amet.<br>✓ Vivamus eu dui ex. Curabitur dapibus.</div>
  <div class="abs txt" style="left:106px;top:31px;width:24px;font-size:2px">✓ Lorem ipsum dolor sit amet.<br>✓ Vivamus eu dui ex. Curabitur dapibus.</div>
  <div class="abs txt" style="left:171px;top:31px;width:24px;font-size:2px">✓ Lorem ipsum dolor sit amet.<br>✓ Vivamus eu dui ex. Curabitur dapibus.</div>
  <div class="tl-text" style="left:42px;top:49px;color:var(--purple-mid)">Heading<br>Goes Here!</div>
  <div class="tl-text" style="left:106px;top:49px;color:var(--pink)">Heading<br>Goes Here!</div>
  <div class="tl-text" style="left:171px;top:49px;color:var(--violet)">Heading<br>Goes Here!</div>
  <div class="tl-dot" style="left:20px;background:var(--blue)">1</div>
  <div class="tl-dot" style="left:52px;background:var(--purple-mid)">2</div>
  <div class="tl-dot" style="left:85px;background:var(--lilac)">3</div>
  <div class="tl-dot" style="left:117px;background:var(--pink)">4</div>
  <div class="tl-dot" style="left:150px;background:var(--blue-light)">5</div>
  <div class="tl-dot" style="left:182px;background:var(--violet)">6</div>
  <div class="tl-text" style="left:8px;top:72px;color:var(--blue)">Heading<br>Goes Here!</div>
  <div class="tl-text" style="left:73px;top:72px;color:var(--lilac)">Heading<br>Goes Here!</div>
  <div class="tl-text" style="left:138px;top:72px;color:var(--blue-light)">Heading<br>Goes Here!</div>
  <div class="abs txt" style="left:10px;top:82px;width:24px;font-size:2px">✓ Lorem ipsum dolor sit amet.<br>✓ Vivamus eu dui ex. Curabitur dapibus.</div>
  <div class="abs txt" style="left:75px;top:82px;width:24px;font-size:2px">✓ Lorem ipsum dolor sit amet.<br>✓ Vivamus eu dui ex. Curabitur dapibus.</div>
  <div class="abs txt" style="left:140px;top:82px;width:24px;font-size:2px">✓ Lorem ipsum dolor sit amet.<br>✓ Vivamus eu dui ex. Curabitur dapibus.</div>
  <div class="footer">© 2021 Corvath Therapeutics, All Rights Reserved.<span class="page">11</span></div>
</section>

<section class="slide" style="left:450px;top:816px">
  <h2 class="slide-title">Column <em style="color:var(--blue)">Chart</em> <em>Slide</em></h2>
  <div class="mini-brand"><i></i>Corvath</div>
  <svg class="abs" style="left:14px;top:36px" width="115" height="60" viewBox="0 0 115 60">
    <g font-size="2" fill="#666" font-family="Lexend, sans-serif">
      <text x="0" y="2">6</text><text x="0" y="10">5</text><text x="0" y="18">4</text><text x="0" y="26">3</text><text x="0" y="34">2</text><text x="0" y="42">1</text><text x="0" y="50">0</text>
      <text x="12" y="54">Kategorie 1</text><text x="36" y="54">Kategorie 2</text><text x="60" y="54">Kategorie 3</text><text x="84" y="54">Kategorie 4</text>
      <text x="38" y="58">● Serie 1 ● Serie 2 ● Serie 3</text>
    </g>
    <line x1="6" y1="49.5" x2="110" y2="49.5" stroke="#ccc" stroke-width=".3"/>
    <rect x="14" y="14" width="3.5" height="35.5" fill="#0054AA"/><rect x="18.5" y="30" width="3.5" height="19.5" fill="#B969AE"/><rect x="23" y="34" width="3.5" height="15.5" fill="#D3A5CF"/>
    <rect x="38" y="30" width="3.5" height="19.5" fill="#0054AA"/><rect x="42.5" y="13" width="3.5" height="36.5" fill="#B969AE"/><rect x="47" y="34" width="3.5" height="15.5" fill="#D3A5CF"/>
    <rect x="62" y="22" width="3.5" height="27.5" fill="#0054AA"/><rect x="66.5" y="35" width="3.5" height="14.5" fill="#B969AE"/><rect x="71" y="25" width="3.5" height="24.5" fill="#D3A5CF"/>
    <rect x="86" y="12" width="3.5" height="37.5" fill="#0054AA"/><rect x="90.5" y="28" width="3.5" height="21.5" fill="#B969AE"/><rect x="95" y="8" width="3.5" height="41.5" fill="#D3A5CF"/>
  </svg>
  <div class="abs" style="left:128px;top:37px;width:70px">
    <div style="display:flex;gap:2px;align-items:center;font-size:3.6px" class="h-blue"><i style="width:4px;height:4px;background:var(--blue)"></i>Title Goes Here!</div>
    <div class="txt" style="font-size:2.1px;padding-left:8px;margin-bottom:5px">Lorem ipsum dolor sit amet, consectetur adipiscing elit. Vivamus eu dui ex. Curabitur dapibus dignissim dui.</div>
    <div style="display:flex;gap:2px;align-items:center;font-size:3.6px" class="h-purple"><i style="width:4px;height:4px;background:var(--purple-mid)"></i>Title Goes Here!</div>
    <div class="txt" style="font-size:2.1px;padding-left:8px;margin-bottom:5px">Lorem ipsum dolor sit amet, consectetur adipiscing elit. Vivamus eu dui ex. Curabitur dapibus dignissim dui.</div>
    <div style="display:flex;gap:2px;align-items:center;font-size:3.6px" class="h-lilac"><i style="width:4px;height:4px;background:var(--lilac)"></i>Title Goes Here!</div>
    <div class="txt" style="font-size:2.1px;padding-left:8px">Lorem ipsum dolor sit amet, consectetur adipiscing elit. Vivamus eu dui ex. Curabitur dapibus dignissim dui.</div>
  </div>
  <div class="footer">© 2021 Corvath Therapeutics, All Rights Reserved.<span class="page">12</span></div>
</section>

<!-- row 5 -->
<section class="slide" style="left:15px;top:942px">
  <h2 class="slide-title">Pie <em style="color:var(--blue)">Chart</em> <em>Slide</em></h2>
  <div class="mini-brand"><i></i>Corvath</div>
  <div class="abs" style="left:0;top:40px;width:90px;height:23px;background:var(--grey-light)"></div>
  <div class="abs" style="left:0;top:68px;width:90px;height:23px;background:var(--grey-light)"></div>
  <div class="abs" style="left:120px;top:40px;width:90px;height:23px;background:var(--grey-light)"></div>
  <div class="abs" style="left:120px;top:68px;width:90px;height:23px;background:var(--grey-light)"></div>
  <div class="abs" style="left:0;top:40px;width:8px;height:23px;background:var(--pink);color:#fff;font-size:4px;writing-mode:vertical-rl;transform:rotate(180deg);text-align:center">20%</div>
  <div class="abs" style="left:0;top:68px;width:8px;height:23px;background:var(--lilac);color:#fff;font-size:4px;writing-mode:vertical-rl;transform:rotate(180deg);text-align:center">40%</div>
  <div class="abs" style="left:202px;top:40px;width:8px;height:23px;background:var(--blue);color:#fff;font-size:4px;writing-mode:vertical-rl;transform:rotate(180deg);text-align:center">80%</div>
  <div class="abs" style="left:202px;top:68px;width:8px;height:23px;background:var(--purple-mid);color:#fff;font-size:4px;writing-mode:vertical-rl;transform:rotate(180deg);text-align:center">60%</div>
  <div class="abs" style="left:18px;top:42px;width:40px;text-align:center"><div style="font-size:3.8px;color:var(--pink)">Heading</div><div class="txt" style="font-size:2px">Lorem ipsum dolor sit amet, consectetur adipiscing elit. Vivamus eu dui ex.</div></div>
  <div class="abs" style="left:18px;top:70px;width:40px;text-align:center"><div style="font-size:3.8px;color:var(--lilac)">Heading</div><div class="txt" style="font-size:2px">Lorem ipsum dolor sit amet, consectetur adipiscing elit. Vivamus eu dui ex.</div></div>
  <div class="abs" style="left:152px;top:42px;width:40px;text-align:center"><div style="font-size:3.8px;color:var(--blue)">Heading</div><div class="txt" style="font-size:2px">Lorem ipsum dolor sit amet, consectetur adipiscing elit. Vivamus eu dui ex.</div></div>
  <div class="abs" style="left:152px;top:70px;width:40px;text-align:center"><div style="font-size:3.8px;color:var(--purple-mid)">Heading</div><div class="txt" style="font-size:2px">Lorem ipsum dolor sit amet, consectetur adipiscing elit. Vivamus eu dui ex.</div></div>
  <svg class="abs" style="left:0;top:0" width="210" height="118" viewBox="0 0 210 118">
    <circle cx="105" cy="62" r="31" fill="#fff"/>
    <path d="M105,62 L105,35 A27,27 0 0 1 113.3,87.7 Z" fill="#0054AA"/>
    <path d="M105,62 L113.3,87.7 A27,27 0 0 1 78,62 Z" fill="#B969AE"/>
    <path d="M105,62 L78,62 A27,27 0 0 1 89.1,40.2 Z" fill="#D3A5CF"/>
    <path d="M105,62 L89.1,40.2 A27,27 0 0 1 105,35 Z" fill="#E54698"/>
    <g font-size="3.3" fill="#fff" font-family="Lexend, sans-serif">
      <text x="117" y="61">80%</text><text x="96" y="41">20%</text><text x="82" y="56">40%</text><text x="95" y="83">60%</text>
    </g>
  </svg>
  <div class="footer">© 2021 Corvath Therapeutics, All Rights Reserved.<span class="page">13</span></div>
</section>

<section class="slide" style="left:232px;top:942px">
  <h2 class="slide-title">Table <em>Slide</em></h2>
  <div class="mini-brand"><i></i>Corvath</div>
  <div class="abs" style="left:16px;top:32px;width:45px;height:25px;background:var(--blue);color:#fff;font-size:6.5px;line-height:1.05;padding:5px 3px">Title Goes<br>Here!</div>
  <div class="abs" style="left:61px;top:32px;width:45px;height:6px;background:var(--purple-mid);color:#fff;font-size:2.4px;text-align:center;line-height:6px">Heading 1</div>
  <div class="abs" style="left:106px;top:32px;width:45px;height:6px;background:var(--lilac);color:#fff;font-size:2.4px;text-align:center;line-height:6px">Heading 2</div>
  <div class="abs" style="left:151px;top:32px;width:45px;height:6px;background:var(--pink);color:#fff;font-size:2.4px;text-align:center;line-height:6px">Heading 3</div>
  <div class="abs" style="left:61px;top:38.5px;width:45px;height:12px;background:var(--purple);color:#fff;font-size:7px;text-align:center;line-height:12px">2019</div>
  <div class="abs" style="left:106px;top:38.5px;width:45px;height:12px;background:var(--purple-mid);color:#fff;font-size:7px;text-align:center;line-height:12px">2020</div>
  <div class="abs" style="left:151px;top:38.5px;width:45px;height:12px;background:var(--pink);color:#fff;font-size:7px;text-align:center;line-height:12px">2021</div>
  <div class="abs" style="left:61px;top:51px;width:45px;height:5px;background:var(--purple-mid);color:#fff;font-size:2px;text-align:center;line-height:5px">Text Goes Here</div>
  <div class="abs" style="left:106px;top:51px;width:45px;height:5px;background:var(--lilac);color:#fff;font-size:2px;text-align:center;line-height:5px">Text Goes Here</div>
  <div class="abs" style="left:151px;top:51px;width:45px;height:5px;background:var(--pink);color:#fff;font-size:2px;text-align:center;line-height:5px">Text Goes Here</div>
  <table class="data" style="top:58px;width:180px">
    <tr><td style="width:45px">Text Goes Here</td><td style="color:var(--purple)">✓</td><td style="color:var(--purple-mid)">✓</td><td>✓</td></tr>
    <tr><td>Text Goes Here</td><td style="color:var(--purple)">✓</td><td style="color:var(--purple-mid)">✓</td><td>✓</td></tr>
    <tr><td>Text Goes Here</td><td style="color:var(--purple)">✓</td><td style="color:var(--purple-mid)">✓</td><td>✓</td></tr>
    <tr><td>Text Goes Here</td><td></td><td style="color:var(--purple-mid)">✓</td><td>✓</td></tr>
    <tr><td>Text Goes Here</td><td></td><td></td><td>✓</td></tr>
  </table>
  <div class="abs" style="left:61px;top:92px;width:45px;height:5px;background:var(--purple-mid);color:#fff;font-size:2px;text-align:center;line-height:5px">Text Goes Here</div>
  <div class="abs" style="left:106px;top:92px;width:45px;height:5px;background:var(--lilac);color:#fff;font-size:2px;text-align:center;line-height:5px">Text Goes Here</div>
  <div class="abs" style="left:151px;top:92px;width:45px;height:5px;background:var(--pink);color:#fff;font-size:2px;text-align:center;line-height:5px">Text Goes Here</div>
  <div class="abs" style="left:16px;top:92px;width:45px;height:5px;background:var(--blue)"></div>
  <div class="footer">© 2021 Corvath Therapeutics, All Rights Reserved.<span class="page">14</span></div>
</section>

<section class="slide" style="left:450px;top:942px">
  <h2 class="slide-title">Slide Title <em>Goes Here</em></h2>
  <div class="mini-brand"><i></i>Corvath</div>
  <div class="photo" role="img" aria-label="Photo of hands using a tablet" style="left:0;top:30px;width:70px;height:70px;background:linear-gradient(135deg,#c4c8cf,#5b6577)"></div>
  <div class="abs" style="left:75px;top:30px;width:61px;height:70px;background:var(--blue);color:#fff;padding:4px 7px"><div style="font-size:11px;font-weight:600;line-height:1">“</div><div style="font-size:3.2px;line-height:1.2;margin-top:5px">Lorem ipsum dolor sit amet, consectetur adipiscing elit. Vivamus eu dui ex. Curabitur dapibus dignissim dui, in molestie metus feugiat sed. Praesent aliquet lorem ex, eu dapibus odio varius at.</div></div>
  <div class="abs" style="left:141px;top:30px;width:61px;height:70px;background:var(--purple-mid);color:#fff;padding:4px 7px"><div style="font-size:11px;font-weight:600;line-height:1">“</div><div style="font-size:3.2px;line-height:1.2;margin-top:5px">Lorem ipsum dolor sit amet, consectetur adipiscing elit. Vivamus eu dui ex. Curabitur dapibus dignissim dui, in molestie metus feugiat sed. Praesent aliquet lorem ex, eu dapibus odio varius at.</div></div>
  <div class="footer">© 2021 Corvath Therapeutics, All Rights Reserved.<span class="page">15</span></div>
</section>

<!-- row 6: contact -->
<section class="slide" style="left:232px;top:1067px;background:linear-gradient(160deg,#17356b,#0c1d3d 60%,#0a1530)">
  <svg class="abs" width="210" height="118" viewBox="0 0 210 118" role="img" aria-label="Faded photo of city towers behind blue overlay">
    <rect x="120" y="0" width="90" height="118" fill="#2b4470" opacity=".45"/>
    <polygon points="110,0 150,0 180,40 168,40" fill="#B969AE" opacity=".35"/>
    <polygon points="140,118 165,118 200,70 188,62" fill="#0677BA" opacity=".35"/>
  </svg>
  <div class="cover-brand" style="left:20px;top:48px;color:#fff"><i style="background:#fff"></i>Corvath Therapeutics</div>
  <div class="abs" style="left:20px;top:64px;font-size:5px;color:#fff">Contact Us</div>
  <div class="abs" style="left:20px;top:72px;font-size:2.4px;color:#fff">Insert Company Address Here!</div>
  <div class="abs" style="left:20px;top:80px">
    <div class="contact-line"><svg width="3" height="3" viewBox="0 0 10 10"><path d="M2 1 L4 1 L5 3 L3.5 4.2 Q5 6.5 6 6.5 L7 5 L9 6 L9 8 Q8 9 6.5 9 Q1 7 1 2 Z" fill="#fff"/></svg>Insert Phone Number</div>
    <div class="contact-line"><svg width="3" height="3" viewBox="0 0 10 10"><circle cx="5" cy="5" r="3.8" fill="none" stroke="#fff" stroke-width="1.2"/><circle cx="5" cy="5" r="1.5" fill="#fff"/></svg>Insert E-Mail Address</div>
    <div class="contact-line"><svg width="3" height="3" viewBox="0 0 10 10"><circle cx="5" cy="5" r="4" fill="none" stroke="#fff" stroke-width="1"/><line x1="1" y1="5" x2="9" y2="5" stroke="#fff" stroke-width=".8"/><ellipse cx="5" cy="5" rx="1.8" ry="4" fill="none" stroke="#fff" stroke-width=".8"/></svg>Insert URL Address</div>
  </div>
  <div class="abs" style="left:0;right:0;bottom:3px;text-align:center;font-size:1.8px;color:#fff">© 2021 Corvath Therapeutics, All Rights Reserved.</div>
</section>

</body>
</html>
```